Wordpress Design Project (Halvern)

We need a wordpress design for an established auction and real estate company based in Virginia. The winning design will incorporate the colors of logo (red and black) creatively with an accent color in a very professional and clean layout.

Industry/Entity Type

Real Estate

Requirements
Must have
• We will require winning designer to provide a layered PSD (Adobe photoshop) concept file, along with any non-standard font files used.

Horizontal Navigation menu with these links:
Home - Upcoming Auctions - Past Auctions - For Sale- Consignments - About Us - Highlights - Contact Us

A slideshow element on the home page using the placeholder image provided.

Sidebar widgets to be included are: Email sign-up form - Featured Auctions - Featured Assets for Sale (see attached for visual of these widgets)

attached logos in footer with company contact info

```html
<!DOCTYPE html>
<html lang="en">
<head>
<meta charset="utf-8">
<title>Halvern Enterprises – Auctions &amp; Real Estate</title>
<link href="https://fonts.googleapis.com/css2?family=Roboto+Condensed:wght@400;700&family=Arimo:wght@400;700&display=swap" rel="stylesheet">
<style>
:root{
  --red:#f12d1f;
  --red-deep:#d9210f;
  --ink:#230503;
  --text:#222222;
  --page:#efefef;
  --card:#ffffff;
  --panel:#f7f7f7;
  --line:#dddddd;
  --muted:#555555;
}
*{box-sizing:border-box;margin:0;padding:0}
html,body{width:1087px;height:1200px;overflow:hidden}
body{background:var(--page);font-family:"Arimo",Arial,sans-serif;color:var(--text);position:relative}
.abs{position:absolute}

/* header */
.brand{left:130px;top:26px;display:flex;align-items:center;gap:10px}
.brand-mark{width:38px;height:38px;background:var(--red)}
.brand-name{font-family:"Roboto Condensed",sans-serif;font-weight:700;font-size:34px;color:var(--ink);letter-spacing:.5px}
.call{left:616px;top:39px;font-family:"Roboto Condensed",sans-serif;font-size:24px;color:var(--ink)}
.call span{color:var(--red);font-size:19px}
.social{left:844px;top:39px;display:flex;gap:4px}
.social i{display:block;width:25px;height:25px;border-radius:50%;background:var(--ink)}

/* navigation */
.nav{left:0;top:95px;width:1087px;height:43px;background:var(--ink)}
.nav a{position:absolute;top:16px;color:#fff;text-decoration:none;font-weight:700;font-size:10.5px}
.nav .active-bar{position:absolute;left:344px;top:0;width:122px;height:3px;background:var(--red)}
.dropdown{left:344px;top:138px;width:122px;height:105px;background:var(--red);border-radius:0 0 5px 5px;overflow:hidden;z-index:2}
.dropdown a{display:block;height:24px;line-height:24px;padding-left:10px;color:#fff;font-weight:700;font-size:10.5px;text-decoration:none;border-bottom:1px solid #ff5a4c}
.dropdown a.current{background:var(--ink);border-bottom-color:var(--ink)}

/* hero */
.hero{left:127px;top:138px;width:833px;height:291px;background:var(--card);border-radius:0 0 4px 4px}
.slide{left:135px;top:138px;width:583px;height:282px;background:linear-gradient(180deg,#dfe8ee 0%,#b9c9d3 30%,#8a9ba4 45%,#7d8d78 65%,#6d8a3c 82%,#55732a 100%);border-radius:0 0 0 4px}
.signup{left:718px;top:138px;width:234px;height:282px;background:var(--red);border-radius:0 0 4px 0;color:#fff;padding:0 0 0 19px}
.signup h2{font-family:"Roboto Condensed",sans-serif;font-weight:400;font-size:25px;margin-top:17px}
.signup label{position:absolute;left:19px;font-size:11.5px}
.signup .field{position:absolute;left:19px;width:195px;height:24px;background:#fff}
.subscribe{position:absolute;left:128px;top:233px;width:88px;height:27px;background:var(--ink);border-radius:4px;color:#fff;font-family:"Roboto Condensed",sans-serif;font-size:16px;text-align:center;line-height:27px}

/* welcome */
.main{left:127px;top:452px;width:572px;height:629px;background:var(--card);border:1px solid #e6e6e6;border-radius:4px}
.welcome-title{left:137px;top:463px;font-family:"Roboto Condensed",sans-serif;font-weight:400;font-size:19px;color:#333}
.welcome-copy{left:138px;top:491px;width:549px;font-size:11.3px;line-height:15px;text-align:justify;color:#222}

/* upcoming */
.upcoming-head{left:137px;top:608px;width:553px;height:43px;background:var(--ink);border-radius:4px 4px 0 0;color:#fff;font-family:"Roboto Condensed",sans-serif;font-size:20px;padding:8px 0 0 9px}
.upcoming-body{left:137px;top:651px;width:553px;height:404px;background:var(--panel);border:1px solid #e4e4e4;border-top:0;border-radius:0 0 4px 4px}
.lot{left:149px;width:540px;height:180px}
.lot-photo{position:absolute;left:0;top:0;width:124px;height:84px;background:linear-gradient(160deg,#9bb4c6 0%,#c9cfd3 40%,#9fa3a3 60%,#5f7a3e 100%);border:3px solid #3a3a3a}
.lot-title{position:absolute;left:133px;top:2px;font-family:"Roboto Condensed",sans-serif;font-weight:400;font-size:19px;color:var(--red)}
.lot-text{position:absolute;left:133px;top:26px;width:396px;font-size:11.3px;line-height:15px;text-align:justify;color:#333}
.btn{position:absolute;left:0;width:124px;height:25px;border-radius:4px;color:#fff;font-family:"Roboto Condensed",sans-serif;font-size:16px;display:flex;align-items:center;gap:10px;padding-left:15px}
.btn.details{top:92px;background:var(--red)}
.btn.photos{top:132px;background:var(--ink)}
.meta-h{position:absolute;left:131px;font-family:"Roboto Condensed",sans-serif;font-size:15px;color:var(--red)}
.meta-t{position:absolute;left:131px;font-size:11px;color:#333}
.sep{left:149px;width:530px;height:1px;background:var(--line);top:853px}

/* sidebar */
.widget{left:719px;width:241px;background:var(--card);border:1px solid #e6e6e6;border-radius:4px}
.widget-head{position:absolute;left:-1px;top:-1px;width:241px;height:40px;background:linear-gradient(180deg,var(--red),var(--red-deep));border-radius:4px 4px 0 0;color:#fff;font-family:"Roboto Condensed",sans-serif;font-size:20px;padding:8px 0 0 15px}
.w-photo{position:absolute;width:156px;height:81px;background:linear-gradient(160deg,#9bb4c6 0%,#c9cfd3 40%,#9fa3a3 60%,#5f7a3e 100%);border:4px solid #3a3a3a}
.w-h{position:absolute;font-family:"Roboto Condensed",sans-serif;font-size:15px;color:var(--red)}
.w-t{position:absolute;font-size:11px;color:#222}
.w-addr{position:absolute;font-size:10px;color:#222}
.more{position:absolute;font-weight:700;font-size:10.5px;color:var(--muted);border-bottom:1px solid var(--muted);padding:0 4px 1px 0}

/* footer */
.footer{left:0;top:1114px;width:1087px;height:86px;background:var(--ink);color:#fff;font-size:10px}
.footer .links{position:absolute;left:134px;top:19px}
.footer .copy{position:absolute;left:134px;top:41px}
.badges{position:absolute;left:614px;top:15px;display:flex;align-items:center;gap:10px}
.badges i{display:block;background:#c9c9c9}
</style>
</head>
<body>

<header>
  <div class="abs brand"><span class="brand-mark"></span><span class="brand-name">Halvern Enterprises</span></div>
  <div class="abs call"><span>Call us:</span> 555 014 7290</div>
  <div class="abs social" aria-label="Social links"><i></i><i></i><i></i><i></i></div>
</header>

<nav class="abs nav">
  <span class="active-bar"></span>
  <a style="left:142px">HOME</a>
  <a style="left:211px">UPCOMING AUCTIONS</a>
  <a style="left:360px">PAST AUCTIONS</a>
  <a style="left:479px">FOR SALE</a>
  <a style="left:568px">CONSIGNMENTS</a>
  <a style="left:689px">ABOUT US</a>
  <a style="left:779px">HIGHLIGHTS</a>
  <a style="left:880px">CONTACT US</a>
</nav>
<div class="abs dropdown">
  <a>Past Auction 1</a>
  <a class="current">Past Auction 2</a>
  <a>Past Auction 3</a>
  <a>Past Auction 4</a>
</div>

<section>
  <div class="abs hero"></div>
  <div class="abs slide" role="img" aria-label="Slideshow photo of a river shore with a wooden pier and tall grass"></div>
  <form class="abs signup">
    <h2>Email sign-up form</h2>
    <label style="top:63px">First Name</label><span class="field" style="top:81px"></span>
    <label style="top:121px">Last Name</label><span class="field" style="top:139px"></span>
    <label style="top:175px">Email Address</label><span class="field" style="top:193px"></span>
    <span class="subscribe">Subscribe</span>
  </form>
</section>

<main>
  <div class="abs main"></div>
  <h1 class="abs welcome-title">Welcome to Halvern Enterprises...</h1>
  <p class="abs welcome-copy">simply dummy text of the printing and typesetting industry. Lorem Ipsum has been the industry's standard dummy text ever since the 1500s, when an unknown printer took a galley of type and scrambled it to make a type specimen book. It has survived not only five centuries, but also the leap into electronic typesetting, remaining essentially unchanged. It was popularised in the 1960s with the release of Lettrafix sheets containing Lorem Ipsum passages, and more recently with desktop publishing software like Quillset Layout including versions of Lorem Ipsum.</p>

  <div class="abs upcoming-head">Upcoming Auctions</div>
  <div class="abs upcoming-body"></div>

  <article class="abs lot" style="top:670px">
    <div class="lot-photo" role="img" aria-label="Photo of a silver minivan"></div>
    <h3 class="lot-title">Selling To the Highest Bidder</h3>
    <p class="lot-text">simply dummy text of the printing and typesetting industry. Lorem Ipsum has been the industry's standard dummy text ever since the 1500s, when an unknown printer.</p>
    <span class="btn details"><svg width="17" height="17" viewBox="0 0 17 17"><circle cx="10" cy="7" r="5" fill="none" stroke="#fff" stroke-width="2"/><line x1="6.5" y1="10.5" x2="2" y2="15" stroke="#fff" stroke-width="3" stroke-linecap="round"/></svg>DETAILS</span>
    <span class="btn photos"><svg width="19" height="15" viewBox="0 0 19 15"><rect x="1" y="3" width="17" height="11" rx="2" fill="#fff"/><rect x="3" y="1" width="5" height="3" fill="#fff"/><circle cx="10.5" cy="8.5" r="3.3" fill="var(--ink)"/></svg>PHOTOS</span>
    <span class="meta-h" style="top:89px">Live On Site Auction</span>
    <span class="meta-t" style="top:106px">Begins:&nbsp; Saturday, March 16, 2013 at 10:00 AM EDT</span>
    <span class="meta-h" style="top:131px">Location</span>
    <span class="meta-t" style="top:149px">1180 Cedar Mill, OK 73012</span>
  </article>

  <div class="abs sep"></div>

  <article class="abs lot" style="top:877px">
    <div class="lot-photo" role="img" aria-label="Photo of a silver minivan"></div>
    <h3 class="lot-title">Selling To the Highest Bidder</h3>
    <p class="lot-text">simply dummy text of the printing and typesetting industry. Lorem Ipsum has been the industry's standard dummy text ever since the 1500s, when an unknown printer.</p>
    <span class="btn details"><svg width="17" height="17" viewBox="0 0 17 17"><circle cx="10" cy="7" r="5" fill="none" stroke="#fff" stroke-width="2"/><line x1="6.5" y1="10.5" x2="2" y2="15" stroke="#fff" stroke-width="3" stroke-linecap="round"/></svg>DETAILS</span>
    <span class="btn photos"><svg width="19" height="15" viewBox="0 0 19 15"><rect x="1" y="3" width="17" height="11" rx="2" fill="#fff"/><rect x="3" y="1" width="5" height="3" fill="#fff"/><circle cx="10.5" cy="8.5" r="3.3" fill="var(--ink)"/></svg>PHOTOS</span>
    <span class="meta-h" style="top:89px">Live On Site Auction</span>
    <span class="meta-t" style="top:106px">Begins:&nbsp; Saturday, March 16, 2013 at 10:00 AM EDT</span>
    <span class="meta-h" style="top:131px">Location</span>
    <span class="meta-t" style="top:149px">1180 Cedar Mill, OK 73012</span>
  </article>
</main>

<aside>
  <section class="abs widget" style="top:451px;height:315px">
    <div class="widget-head">Featured Auctions</div>
    <span class="w-h" style="left:13px;top:51px">Session 1</span>
    <span class="w-t" style="left:13px;top:73px">Multi Estate &amp; Consignment Auction.</span>
    <div class="w-photo" style="left:15px;top:96px" role="img" aria-label="Photo of a silver minivan"></div>
    <span class="w-h" style="left:15px;top:186px">Start Date/ Time</span>
    <span class="w-t" style="left:15px;top:209px">Saturday, April 13, 2013 At 10:00 AM</span>
    <span class="w-h" style="left:15px;top:231px">Location</span>
    <span class="w-addr" style="left:16px;top:253px">1180 Cedar Mill, OK 73012</span>
    <span class="more" style="left:15px;top:278px">More Details »</span>
  </section>

  <section class="abs widget" style="top:797px;height:282px">
    <div class="widget-head">Featured Assets for Sale</div>
    <div class="w-photo" style="left:16px;top:60px" role="img" aria-label="Photo of a silver minivan"></div>
    <span class="w-h" style="left:16px;top:150px">Start Date/ Time</span>
    <span class="w-t" style="left:16px;top:173px">Saturday, April 13, 2013 At 10:00 AM</span>
    <span class="w-h" style="left:16px;top:195px">Location</span>
    <span class="w-addr" style="left:17px;top:217px">1180 Cedar Mill, OK 73012</span>
    <span class="more" style="left:16px;top:242px">More Details »</span>
  </section>
</aside>

<footer class="abs footer">
  <div class="links">Home | Upcoming Auctions | Past Auctions | For Sale | Highlights | Contact Us</div>
  <div class="copy">Copyright (C) Halvern&nbsp; Enterprises. 2013.&nbsp; All Rights Reserved</div>
  <div class="badges" aria-label="Partner associations">
    <i style="width:28px;height:32px"></i>
    <i style="width:66px;height:30px;border-radius:4px"></i>
    <i style="width:66px;height:22px;border-radius:4px"></i>
    <i style="width:46px;height:46px;border-radius:50%"></i>
    <i style="width:98px;height:40px;border-radius:4px"></i>
  </div>
</footer>

</body>
</html>
```